Hand made soap for men packaging design

Need packaging concept and mock-up for new product line of handmade bar soaps for men. Please read the attached project brief for packaging requirements and examples. Adobe Illustrator logo files are attached as well.

Our company, Steel And Stone Co.™, specializes in high-end self-care products for men. We focus on the needs of high-performing men in their mid-30’s to 50’s who have worked hard to achieve their goals. We encourage a strong, positive view of masculinity where traits such as courage, bravery, competition, stoicism, toughness, and independence are celebrated.

Our body and skincare products use natural and organic ingredients that are designed to inspire confidence in everything men do, with a distinct focus on anti-aging benefits and enhancement to overall male virility and health. We avoid estrogenics and other ingredients that have been shown to have adverse effects on men’s health, most notably the production of testosterone.

Quartet™ is our initial product line consisting of all-natural handmade soaps that make up a basic daily skin care routine for men in our target niche. This product line is inspired by the Greek philosopher, Aristotle, who was the first to theorize about the four (4) natural elements: Fire, Water, Air and Earth. There are four (4) individual soap variations, each one associated with one of these elements. The alignment of the Quartet™ collection to Ancient Greece perfectly embodies the idea of manhood we promote at Steel And Stone Co.™, with this classical conception of masculinity defining manhood in the West up until the middle of the 20th century.

In addition to Quartet™ there will be additional collections released in the future, each one with it’s own concept, theme and design considerations.

Target Market(s)

Industry/Entity Type

Men's health, body/skin care products

Font styles to use
Sans Serif
Decorative
Other font styles liked:
• Any masculine font that aligns to theme of Ancient Greece

Requirements
Must have
• Project requirements are detailed in the attached MS Word project brief. Please design for one (1) product, but consider that there will be three (3) others designed later to complete the collection. Each product will carry the same general design theme created here.
Nice to have
• This product line is inspired by the Greek philosopher, Aristotle, who was the first to theorize about the four (4) natural elements: Fire, Water, Air and Earth. There are four (4) individual soap variations, each one associated with one of these elements. The alignment of the Quartet™ collection to Ancient Greece perfectly embodies the idea of manhood we promote at Steel And Stone Co.™, with this classical conception of masculinity defining manhood in the West up until the middle of the 20th century. Sample packaging concepts are included in the attached MS Word project brief.

```html
<!DOCTYPE html>
<html lang="en">
<head>
<meta charset="utf-8">
<title>Quartet Fire – Soap Box Dieline</title>
<link rel="stylesheet" href="https://fonts.googleapis.com/css2?family=Cabin:wght@400;500&family=Open+Sans:ital,wght@0,600;1,400&family=Oswald:wght@400;600&display=swap">
<style>
  :root {
    --canvas: #e6e6e6;
    --fire-red: #c80000;
    --deep-red: #a30f0f;
    --shadow-red: #b00808;
    --flap-gold: #f5b942;
    --panel-gold: #d6a23e;
    --ember: #f07d00;
    --ink: #1a1a1a;
    --white: #ffffff;
  }
  html, body {
    margin: 0;
    padding: 0;
    width: 684px;
    height: 1200px;
    overflow: hidden;
    background: var(--canvas);
  }
  .page {
    width: 684px;
    height: 1200px;
    display: flex;
    align-items: center;
    justify-content: center;
  }
  .dieline {
    display: block;
    width: 684px;
    height: 507px;
  }
  .red { fill: var(--fire-red); }
  .flap-gold { fill: var(--flap-gold); }
  .ember { fill: var(--ember); }
  .line-title-small { font-family: "Cabin", sans-serif; font-weight: 400; }
  .line-title-big { font-family: "Cabin", sans-serif; font-weight: 500; }
  .brand-name { font-family: "Oswald", sans-serif; font-weight: 600; }
  .brand-tagline { font-family: "Oswald", sans-serif; font-weight: 400; }
  .blurb { font-family: "Open Sans", sans-serif; font-weight: 600; fill: var(--ink); }
  .ingredients { font-family: "Open Sans", sans-serif; font-style: italic; font-weight: 400; fill: var(--ink); }
</style>
</head>
<body>
<main class="page">
<svg class="dieline" viewBox="0 0 1456 1080" xmlns="http://www.w3.org/2000/svg" aria-label="Flat dieline of the Quartet Fire soap box">
  <defs>
    <radialGradient id="gold-wash" cx="0.6" cy="0.45" r="0.75">
      <stop offset="0" stop-color="#c99a3c"/>
      <stop offset="0.6" stop-color="#d6a23e"/>
      <stop offset="1" stop-color="#e8b24a"/>
    </radialGradient>
  </defs>

  <g class="lid">
    <path class="red" d="M43 127 V70 Q43 38 75 38 H495 Q527 38 527 70 V127 Z"/>
    <rect class="red" x="43" y="127" width="484" height="170"/>
    <polygon class="ember" points="236,127 252,127 462,297 450,297"/>
    <polygon class="flap-gold" points="43,127 240,127 450,297 43,297"/>
    <text class="line-title-small" x="77" y="195" font-size="25" fill="var(--deep-red)">QUARTET</text>
    <text class="line-title-big" x="75" y="240" font-size="58" fill="var(--deep-red)">FIRE</text>
  </g>

  <g class="back-panel">
    <rect class="red" x="43" y="297" width="484" height="485"/>
    <circle cx="283" cy="490" r="44" fill="none" stroke="var(--shadow-red)" stroke-width="6" opacity="0.8"/>
    <text class="brand-name" x="285" y="612" text-anchor="middle" font-size="50" fill="var(--shadow-red)" textLength="372">STEEL AND STONE CO.</text>
    <text class="brand-tagline" x="285" y="640" text-anchor="middle" font-size="22" letter-spacing="3" fill="var(--shadow-red)" textLength="372">FORGED BY DISCIPLINE</text>
  </g>

  <g class="side-panel">
    <path class="red" d="M529 297 V215 Q529 185 559 185 H667 Q697 185 697 215 V297 Z"/>
    <rect class="red" x="527" y="297" width="170" height="485"/>
    <path class="red" d="M529 782 V865 Q529 895 559 895 H667 Q697 895 697 865 V782 Z"/>
    <g transform="translate(582,487) rotate(90)">
      <text class="line-title-small" x="0" y="-43" font-size="24" fill="var(--flap-gold)">QUARTET</text>
      <text class="line-title-big" x="0" y="0" font-size="62" fill="var(--flap-gold)">FIRE</text>
    </g>
  </g>

  <g class="front-panel">
    <rect x="697" y="297" width="488" height="485" fill="url(#gold-wash)"/>
    <polygon class="red" points="697,297 985,297 700,782 697,782"/>
    <polygon class="ember" points="985,297 993,297 708,782 700,782"/>

    <g class="brand-lockup" transform="translate(778,548) rotate(-59.6)">
      <text class="brand-name" x="0" y="0" font-size="38" fill="var(--white)" textLength="280">STEEL AND STONE CO.</text>
      <text class="brand-tagline" x="2" y="20" font-size="15" letter-spacing="1.5" fill="var(--white)" textLength="276">FORGED BY DISCIPLINE</text>
    </g>
    <circle cx="762" cy="585" r="26" fill="none" stroke="var(--white)" stroke-width="5"/>

    <g class="window">
      <polygon points="942,425 805,652 1080,652" fill="var(--fire-red)"/>
      <polygon points="942,443 822,643 1063,643" fill="var(--panel-gold)"/>
      <polygon points="942,458 836,636 1050,636" fill="var(--canvas)"/>
    </g>

    <g class="certification-badge">
      <rect x="1108" y="325" width="48" height="67" rx="6" fill="none" stroke="var(--ink)" stroke-width="3"/>
      <rect x="1117" y="336" width="30" height="44" rx="3" fill="var(--ink)"/>
    </g>

    <text class="line-title-small" x="1157" y="420" text-anchor="end" font-size="25" fill="var(--deep-red)">QUARTET</text>
    <text class="line-title-big" x="1157" y="466" text-anchor="end" font-size="58" fill="var(--deep-red)">FIRE</text>

    <text class="blurb" font-size="15" text-anchor="middle">
      <tspan x="942" y="678">Black pepper, cedar, amber and clove,</tspan>
      <tspan x="942" y="699">come together in a warm and rugged lather</tspan>
      <tspan x="942" y="720">with a hint of embers.</tspan>
    </text>
  </g>

  <path class="flap-gold" d="M700 782 H1185 V1010 Q1185 1042 1153 1042 H732 Q700 1042 700 1010 Z"/>

  <g class="ingredients-panel">
    <path class="flap-gold" d="M1187 297 V215 Q1187 185 1217 185 H1325 Q1355 185 1355 215 V297 Z"/>
    <rect class="flap-gold" x="1185" y="297" width="170" height="485"/>
    <path class="flap-gold" d="M1187 782 V865 Q1187 895 1217 895 H1325 Q1355 895 1355 865 V782 Z"/>
    <g transform="translate(1220,765) rotate(-90)">
      <text class="ingredients" font-size="15">
        <tspan x="0" y="0">Ingredients:</tspan>
        <tspan x="0" y="18">Cold-Process Oils (Sunflower Oil, Organic Castor Oil*, Organic Cocoa</tspan>
        <tspan x="0" y="36">Butter*, Organic Mango Butter*, Jojoba Oil), Charcoal, Scent,</tspan>
        <tspan x="0" y="54">Clove Bud Essential Oil, Kaolin Clay, Sea Salt, Camphor,</tspan>
        <tspan x="0" y="72">Red Clay, Mica. **Ethically Sourced, Small-Batch Cured</tspan>
        <tspan x="0" y="90">By Hand, *Certified Organic</tspan>
      </text>
    </g>
  </g>
</svg>
</main>
</body>
</html>
```